Hollis Ironworks Business Card

We need a business card design for a new small metal fabrication business in rural NSW, Australia.

The business (Hollis Ironworks) is owner operated by a man with the initials RB - much of the branding comes from this name.

Hollis Ironworks designs, engineers, repairs and manufactures a range of custom, quality metal works including vehicle trays, agricultural machinery impliments, trailers, wood splitters, fire pits, furniture etc.

The brand position focuses on custom work of the highest quality.

Business card design should show quality, attention to detail and stand out among a mass of business cards.

Logos are in the files

The grey color may be changed on the logo if required to stand out more.

There is an image attached of a simple card that is liked because it is clean, clear, simple, masculine and effective. It says 'quality'. As most of the work we do is custom it would be good to have the business card speak to this.

Target Market(s)

Rural and regional based Australians. Primarily adult male 25-60 yrs. Primary production / rural / travelling lifestyle.

Industry/Entity Type

Metal Fabrication

Contact Information for Business Card

The words 'custom quality fabrications' would be great somewhere perhaps on the backside (not on the information side)
Name
title
Phone: 0491 538 274 and (02) 7342 9185
email: info@hollisiw.com.au
www.hollisiw.com.au

address (2 lines)

Requirements
Nice to have
• Background colour should be very navy blue or black.
Should not have
• NO orange and blue combinations.
• Navy is OK

```html
<!DOCTYPE html>
<html lang="en">
<head>
<meta charset="utf-8">
<title>Hollis Ironworks Business Card</title>
<link rel="stylesheet" href="https://fonts.googleapis.com/css2?family=Bebas+Neue&family=Open+Sans:wght@400;600&display=swap">
<style>
  :root {
    --backdrop: #d9d6d2;
    --card: #262626;
    --white: #ffffff;
    --text-light: #c9c9c9;
    --steel: #9a9a9a;
    --green: #6cc04a;
  }
  * { margin: 0; padding: 0; box-sizing: border-box; }
  html, body { width: 1200px; height: 1000px; overflow: hidden; }
  body {
    background: var(--backdrop);
    font-family: "Open Sans", Arial, sans-serif;
    position: relative;
  }
  .card {
    position: absolute;
    left: 266px;
    width: 666px;
    height: 397px;
    background: var(--card);
  }
  .card--front { top: 74px; }
  .card--back { top: 533px; }

  .identity {
    position: absolute;
    right: 355px;
    top: 166px;
    text-align: right;
  }
  .identity__name {
    font-family: "Bebas Neue", Impact, sans-serif;
    font-size: 40px;
    line-height: 40px;
    color: var(--white);
    letter-spacing: 0.5px;
  }
  .identity__title {
    font-size: 16px;
    color: var(--green);
    margin-top: 2px;
  }
  .divider {
    position: absolute;
    left: 332px;
    top: 162px;
    width: 2px;
    height: 78px;
    background: var(--white);
  }
  .contacts {
    position: absolute;
    left: 356px;
    top: 152px;
    list-style: none;
  }
  .contacts li {
    display: flex;
    align-items: center;
    height: 22px;
    font-size: 16px;
    color: var(--text-light);
  }
  .contacts svg { width: 15px; height: 15px; margin-right: 7px; fill: var(--green); }
  .address {
    position: absolute;
    left: 0; right: 0;
    top: 348px;
    text-align: center;
    font-size: 15px;
    color: var(--text-light);
  }
  .address__company { color: var(--green); font-weight: 600; }

  .brand {
    position: absolute;
    left: 0; right: 0;
    top: 138px;
    text-align: center;
    font-family: "Open Sans", Arial, sans-serif;
    font-weight: 600;
    font-size: 50px;
    letter-spacing: 3px;
    color: var(--steel);
    text-transform: uppercase;
  }
  .tagline {
    position: absolute;
    left: 92px;
    width: 482px;
    top: 255px;
    display: flex;
    align-items: center;
    justify-content: space-between;
  }
  .tagline__arrow { width: 50px; height: 8px; }
  .tagline__text {
    font-size: 20px;
    letter-spacing: 2.4px;
    color: var(--text-light);
  }
</style>
</head>
<body>
  <section class="card card--front">
    <div class="identity">
      <div class="identity__name">Reid Barlow</div>
      <div class="identity__title">Managing Director</div>
    </div>
    <div class="divider"></div>
    <ul class="contacts">
      <li><svg viewBox="0 0 16 16"><path d="M2 5c0-2 2-3 6-3s6 1 6 3v1h-3V4.5H5V6H2z M3 8h10l1 6H2z"/></svg>0491 538 274</li>
      <li><svg viewBox="0 0 16 16"><path d="M4 1h8v4H4z M1 6h14v6h-3v3H4v-3H1z M5 10v4h6v-4z"/></svg>(02) 7342 9185</li>
      <li><svg viewBox="0 0 16 16"><path d="M1 3h14v1L8 9 1 4z M1 6l7 5 7-5v7H1z"/></svg>info@hollisiw.com.au</li>
      <li><svg viewBox="0 0 16 16"><path d="M8 1a7 7 0 1 0 0 14A7 7 0 0 0 8 1zm0 2a5 5 0 0 1 0 10A5 5 0 0 1 8 3z M6 5h4v2H8v4H6z"/></svg>www.hollisiw.com.au</li>
    </ul>
    <p class="address"><span class="address__company">Hollis Ironworks</span> - PO Box 482 - 14 Kellow Rd Ardlethan, NSW 2665</p>
  </section>

  <section class="card card--back">
    <div class="brand">Hollis Ironworks</div>
    <div class="tagline">
      <svg class="tagline__arrow" viewBox="0 0 50 8"><path d="M0 4L50 0V8z" fill="#6cc04a"/></svg>
      <span class="tagline__text">CUSTOM METAL FABRICATION</span>
      <svg class="tagline__arrow" viewBox="0 0 50 8"><path d="M50 4L0 0V8z" fill="#6cc04a"/></svg>
    </div>
  </section>
</body>
</html>
```